BENEATH THE [HARBOR] OF A DAWN, Mend your road

We are looking for a cover refresh of an existing bestselling book that is going into 3rd edition print this year.
The book is an inspirational as well as educational book that has become recognized as one of the most comprehensive, actionable, personal and financial planning resources available today for families, individuals and business owners alike.
Comprised of three true stories of loss, learning to live and love again and a 30 page checklist at the back of the book it contains tips and strategies for everyone to help them to get their personal and financial lives in order while they can.
The cover must have the following:
1. Appeal to a broad audience/both personal and corporate
2. Include Mara Quellton Bestselling Author
3. Include introduction of a new Afterword
4. 3rd Edition
5. Colors to remain the same – red, black and white
6. The title must remain in caps and the word [HARBOR] must have the brackets around it
We have also added a current copy of the second edition to help you. For your information our website is www.thequelltonhouse.example
Reason: We have narrowed it down to our top 3 designs. We are submitting the covers to our community for them to pick the top cover. Good luck to everyone

```html
<!DOCTYPE html>
<html lang="en">
<head>
<meta charset="utf-8">
<title>Beneath the Harbor of a Dawn — Book Cover</title>
<link rel="stylesheet" href="https://fonts.googleapis.com/css2?family=Bebas+Neue&family=Montserrat:wght@400;700&family=Mr+Dafoe&display=swap">
<style>
  :root {
    --page-bg: #ececec;
    --cover-top: #ffffff;
    --cover-mid: #ece8e3;
    --cover-bottom: #d8d0c6;
    --brand-red: #c1272d;
    --ink-black: #1c1a1a;
    --ink-white: #ffffff;
    --nib-light: #e7c9a0;
    --nib-dark: #8a5a2e;
  }
  html, body {
    margin: 0;
    padding: 0;
    width: 1200px;
    height: 801px;
    overflow: hidden;
    background: var(--page-bg);
  }
  .cover {
    position: absolute;
    left: 347px;
    top: 20px;
    width: 506px;
    height: 760px;
    overflow: hidden;
    background: linear-gradient(180deg, var(--cover-top) 0%, var(--cover-mid) 40%, var(--cover-bottom) 100%);
    box-shadow: 0 10px 24px rgba(0,0,0,0.18);
  }
  .cover__art {
    position: absolute;
    left: 40px;
    top: 0;
    width: 466px;
    height: 300px;
    background: radial-gradient(ellipse at 70% 35%, var(--nib-light) 0%, var(--nib-dark) 40%, rgba(255,255,255,0) 72%);
    clip-path: polygon(100% 0, 100% 78%, 0 88%, 30% 40%, 70% 0);
  }
  .edition-tag {
    position: absolute;
    left: 41px;
    top: 0;
    width: 107px;
    height: 43px;
    background: var(--brand-red);
    color: var(--ink-white);
    font: 700 14px/43px "Montserrat", sans-serif;
    text-align: center;
  }
  .edition-tag sup { font-size: 8px; }
  .afterword-note {
    position: absolute;
    left: 41px;
    top: 51px;
    margin: 0;
    color: var(--ink-black);
    font: 400 15px/19px "Montserrat", sans-serif;
    letter-spacing: 3.2px;
    text-transform: uppercase;
  }
  .title {
    position: absolute;
    left: 0;
    top: 290px;
    width: 100%;
    margin: 0;
    text-align: center;
    font-family: "Bebas Neue", sans-serif;
    font-weight: 400;
    color: var(--ink-black);
  }
  .title__line { display: block; line-height: 1; }
  .title__small { font-size: 62px; letter-spacing: -1px; }
  .title__key {
    font-size: 172px;
    letter-spacing: -3px;
    color: var(--brand-red);
    line-height: 0.82;
    margin: 2px 0 4px;
  }
  .title__key .accent { color: var(--ink-black); }
  .tagline {
    position: absolute;
    left: 0;
    top: 575px;
    width: 100%;
    margin: 0;
    text-align: center;
    font: 400 46px/1 "Mr Dafoe", cursive;
    color: var(--ink-black);
  }
  .author-band {
    position: absolute;
    left: 0;
    bottom: 0;
    width: 100%;
    height: 61px;
    background: var(--brand-red);
    color: var(--ink-white);
    font: 700 31px/61px "Montserrat", sans-serif;
    letter-spacing: 3px;
    text-align: center;
  }
</style>
</head>
<body>
  <main class="cover">
    <div class="cover__art" role="img" aria-label="Close-up photograph of a gold fountain pen nib"></div>
    <div class="edition-tag">3<sup>RD</sup> EDITION</div>
    <p class="afterword-note">Introduction<br>of a new<br>afterword</p>
    <h1 class="title">
      <span class="title__line title__small">Beneath the</span>
      <span class="title__line title__key">[HARB<span class="accent">O</span>R]</span>
      <span class="title__line title__small">Of a dawn</span>
    </h1>
    <p class="tagline">Mend your road</p>
    <div class="author-band">MARA QUELLTON</div>
  </main>
</body>
</html>
```